見本のチラシがありますので、構成とレイアウトは流用していただき、ブラッシュアップしたデザインを期待します。

カラーパレットは以下です。

#F9F4EA
#FFFFFF
#444444
#666666
#F0E3CA
#DB887F
#E4BE7B
#83B2A6

ウェブサイトとロゴの仮デザインもお送りいたします。
チラシは統一感はそこまで必要ないですが、ご参考ください。

また画像は既存園のウェブサイトより流用していただければと思います。

https://kurumiya-hoiku.jp/
見本チラシとの差異をお送りいたします。

ロゴ

月額保育料
平日9:00〜16:00 週3日  0円
平日9:00〜18:00 週5日  10,000円

2021年3月開演予定

まかろん保育園 東戸塚
〒231-0917 神奈川県横浜市戸塚区柳瀬町718-6
MK「東戸塚駅」より徒歩13分

http://makahoiku.jp/lp

株式会社ルナメル
神奈川県横浜市神奈川区緑丘町8-7
横浜リバーテラスビル14階

ーーーーー

見本チラシに追加の要素です。

系列園「くるみや保育園」
https://kurumiya-hoiku.jp/

保育士募集は少し大きめにお願いします。
「詳細はお問い合わせください」「045-731-5184」「担当:森岡」のキーワードをお願いします。
A4
片面
黄・オレンジ系
AIデータに加えて、印刷所へ納品する入稿データまでお願いいたします。
13日中に提案していただいた案を優先いたします。
最終納品は14日の15時と考えております。
よろしくお願い申し上げます。

集まりが悪かった場合は17日まで延期いたします。
http://makahoiku.jp/lp

https://makahoiku.jp/lp

URLがSSLになっておりませんでした。
よろしくお願い申し上げます。

要件を最も満たしていました。デザインのクオリティも素晴らしかったです。

コンペに参加していただきまして、ありがとうございます。
またよろしくお願い申し上げます。

```html
<!DOCTYPE html>
<html lang="ja">
<head>
<meta charset="utf-8">
<title>まかろん保育園 東戸塚 園児募集</title>
<link rel="stylesheet" href="https://fonts.googleapis.com/css2?family=M+PLUS+Rounded+1c:wght@500;700;800;900&family=Zen+Maru+Gothic:wght@500;700;900&display=swap">
<style>
:root{
  --cream:#F9F4EA;
  --white:#FFFFFF;
  --ink:#444444;
  --ink-soft:#666666;
  --beige:#F0E3CA;
  --rose:#DB887F;
  --gold:#E4BE7B;
  --teal:#83B2A6;
}
*{margin:0;padding:0;box-sizing:border-box}
html,body{width:848px;height:1200px;overflow:hidden;background:var(--cream)}
body{font-family:"Zen Maru Gothic","M PLUS Rounded 1c",sans-serif;color:var(--ink)}
.flyer{position:relative;width:848px;height:1200px;background:var(--cream);overflow:hidden}
.abs{position:absolute}
.round{font-family:"M PLUS Rounded 1c",sans-serif}

/* header */
.tag{top:28px;height:46px;padding:0 22px;border-radius:23px;background:var(--white);color:var(--rose);font-size:28px;font-weight:900;line-height:46px;letter-spacing:2px}
.tag--left{left:30px}
.tag--right{right:30px}
.brand{left:334px;top:14px;width:180px;height:150px;border-radius:50%;background:var(--white);text-align:center}
.brand__dot{display:block;width:34px;height:34px;border-radius:50%;background:var(--gold);margin:22px auto 10px}
.brand__name{font-size:34px;font-weight:900;color:var(--rose);line-height:1}
.brand__sub{margin-top:8px;font-size:12px;color:var(--ink-soft);font-weight:700}

.headline{top:180px;font-size:110px;font-weight:900;color:var(--rose);letter-spacing:6px;line-height:1}
.headline span{display:inline-block;width:124px;height:124px;margin-right:10px;background:var(--white);border-radius:18px;text-align:center;line-height:124px;font-size:96px}
.headline--left{left:30px}
.headline--right{right:20px}

.badge{border-radius:50%;color:var(--white);text-align:center;font-weight:900;display:flex;flex-direction:column;justify-content:center;align-items:center;line-height:1.3;white-space:nowrap}
.badge--infant{left:722px;top:80px;width:96px;height:96px;background:var(--rose);font-size:13px;border:4px solid var(--white)}

/* opening & visuals */
.opening{left:30px;top:330px;color:var(--rose);font-weight:900;line-height:1.1}
.opening__date{font-size:40px;background:var(--white);padding:6px 12px;border-radius:10px;display:inline-block}
.opening__label{font-size:54px;margin-top:8px;color:var(--ink)}

.map{left:30px;top:470px;width:220px;height:140px;border-radius:12px;background:linear-gradient(135deg,var(--white),var(--beige));border:2px solid var(--beige)}
.map__label{left:112px;top:548px;background:var(--rose);color:var(--white);font-size:13px;font-weight:700;padding:4px 8px;border-radius:6px;line-height:1.3}
.map__address{left:36px;top:480px;font-size:9px;color:var(--ink-soft);line-height:1.4}

.photo{border-radius:18px;border:6px solid var(--white)}
.photo--center{left:262px;top:330px;width:262px;height:282px;background:linear-gradient(160deg,#f3d7c9,#e7c28a)}
.photo--right{left:540px;top:330px;width:280px;height:230px;background:linear-gradient(160deg,#f0e3ca,#cfe0d8)}
.badge--visit{left:240px;top:296px;width:96px;height:96px;background:var(--gold);font-size:19px;border:4px solid var(--white)}
.badge--capacity{left:676px;top:488px;width:150px;height:150px;background:var(--teal);font-size:14px;border:4px solid var(--white);line-height:1.35}
.badge--capacity b{font-size:24px}

/* fees */
.fees-title{left:30px;top:628px;display:flex;align-items:baseline;gap:12px}
.fees-title__main{background:var(--gold);color:var(--white);font-size:34px;font-weight:900;padding:2px 18px;border-radius:24px}
.fees-title__note{font-size:17px;font-weight:700;color:var(--ink)}
.fee{top:688px;height:146px;background:var(--white);border-radius:14px;border:3px solid var(--beige);padding:12px 18px}
.fee--general{left:30px;width:388px}
.fee--staff{left:430px;width:388px;border-color:var(--teal)}
.fee__head{font-size:22px;font-weight:900;color:var(--rose);line-height:1.2}
.fee--staff .fee__head{color:var(--teal);font-size:19px}
.fee__head small{font-size:14px;color:var(--ink-soft)}
.fee__row{display:flex;justify-content:space-between;align-items:baseline;font-size:17px;font-weight:700;margin-top:6px;border-bottom:2px dotted var(--beige);padding-bottom:2px}
.fee__row b{font-size:26px;color:var(--ink);font-weight:900}
.fee__row b small{font-size:15px}
.fees-notes{left:30px;top:840px;font-size:11px;color:var(--ink-soft);line-height:1.5}

/* site */
.site-name{left:0;top:872px;width:848px;text-align:center;font-size:40px;font-weight:900;color:var(--ink)}
.site-name span{background:var(--rose);color:var(--white);padding:0 10px;border-radius:8px;margin-left:8px;font-size:34px}
.site-lead{left:0;top:927px;width:848px;text-align:center;font-size:18px;font-weight:700;color:var(--ink)}
.site-url{left:84px;top:960px;width:680px;height:64px;background:var(--white);border-radius:32px;border:3px solid var(--gold);display:flex;align-items:center;justify-content:center;gap:14px;font-size:40px;font-weight:800;color:var(--rose);letter-spacing:1px}

/* recruit */
.recruit{left:30px;top:1040px;width:160px;height:100px;background:var(--rose);border-radius:14px;color:var(--white);font-size:32px;font-weight:900;text-align:center;line-height:1.3;padding-top:8px}
.contact{left:204px;top:1042px;line-height:1.3}
.contact__lead{font-size:18px;font-weight:700}
.contact__tel{display:flex;align-items:center;gap:8px;font-size:34px;font-weight:900;color:var(--rose)}
.contact__person{font-size:16px;font-weight:700;color:var(--ink-soft)}
.company{left:30px;top:1150px;line-height:1.3}
.company__name{font-size:18px;font-weight:900}
.company__addr{font-size:11px;color:var(--ink-soft)}

.sister{left:560px;top:1050px;width:258px;text-align:right}
.sister__label{display:inline-block;background:var(--teal);color:var(--white);font-size:14px;font-weight:700;padding:2px 10px;border-radius:12px}
.sister__brand{display:flex;align-items:center;justify-content:flex-end;gap:8px;margin-top:8px;font-size:28px;font-weight:900;color:var(--ink)}
.sister__dot{width:18px;height:18px;border-radius:50%;background:var(--gold)}
.sister__url{margin-top:10px;font-size:18px;font-weight:700;color:var(--ink)}
</style>
</head>
<body>
<main class="flyer">

  <div class="abs tag tag--left">企業主導型</div>
  <div class="abs tag tag--right">小規模保育園</div>
  <div class="abs brand"><span class="brand__dot"></span><div class="brand__name">まかろん</div><div class="brand__sub">企業主導型保育所</div></div>

  <h1 class="abs headline headline--left"><span>園</span><span>児</span></h1>
  <div class="abs headline headline--right"><span>募</span><span>集</span></div>
  <div class="abs badge badge--infant"><span>0歳児クラス</span><span>園児募集中!</span></div>

  <div class="abs opening"><div class="opening__date">2021年3月</div><div class="opening__label">開園予定</div></div>

  <div class="abs map" role="img" aria-label="保育園周辺の案内地図"></div>
  <div class="abs map__address">〒231-0917<br>神奈川県横浜市戸塚区柳瀬町718-6<br>MK「東戸塚駅」より徒歩13分</div>
  <div class="abs map__label">まかろん保育園<br>東戸塚</div>

  <div class="abs photo photo--center" role="img" aria-label="園内で遊ぶ子どもたちの写真"></div>
  <div class="abs photo photo--right" role="img" aria-label="保育室で過ごす子どもたちの写真"></div>
  <div class="abs badge badge--visit"><span>見学も</span><span>可能!</span></div>
  <div class="abs badge badge--capacity"><span>定員<b>00</b>名の</span><span>アットホームな</span><span>保育園です!</span></div>

  <div class="abs fees-title"><span class="fees-title__main">月額保育料</span><span class="fees-title__note">(給食費・教材費を含む)</span></div>
  <section class="abs fee fee--general">
    <div class="fee__head">一般利用 <small>(一例)</small></div>
    <div class="fee__row"><span>平日9:00〜16:00/週3日</span><b>0<small>円</small></b></div>
    <div class="fee__row"><span>平日9:00〜18:00/週5日</span><b>10,000<small>円</small></b></div>
  </section>
  <section class="abs fee fee--staff">
    <div class="fee__head">当社スタッフとして<br>勤務している場合 <small>(一例)</small></div>
    <div class="fee__row"><span>平日9:00〜18:00/週5日</span><b>0<small>円</small></b></div>
  </section>
  <p class="abs fees-notes">※保育料は利用日数や時間により異なります。<br>※詳しくは園までお気軽にご相談ください。</p>

  <h2 class="abs site-name">まかろん保育園<span>東戸塚</span></h2>
  <p class="abs site-lead">入園ご希望の方は下記ホームページをご確認ください!</p>
  <div class="abs site-url round">
    <svg width="34" height="34" viewBox="0 0 24 24" aria-hidden="true"><path d="M5 3l14 8-6 1.5 3.5 6-2.6 1.5-3.5-6L6 18z" fill="#DB887F"/></svg>
    https://makahoiku.jp/lp
  </div>

  <div class="abs recruit">保育士<br>募集</div>
  <div class="abs contact">
    <div class="contact__lead">詳細はお問い合わせください</div>
    <div class="contact__tel round">
      <svg width="28" height="28" viewBox="0 0 24 24" aria-hidden="true"><path d="M6.6 10.8a15 15 0 006.6 6.6l2.2-2.2a1 1 0 011-.25 11.4 11.4 0 003.6.57 1 1 0 011 1V20a1 1 0 01-1 1A17 17 0 013 4a1 1 0 011-1h3.5a1 1 0 011 1 11.4 11.4 0 00.57 3.6 1 1 0 01-.25 1z" fill="#DB887F"/></svg>
      045-731-5184
    </div>
    <div class="contact__person">(担当:森岡)</div>
  </div>
  <div class="abs company">
    <div class="company__name">株式会社ルナメル</div>
    <div class="company__addr">神奈川県横浜市神奈川区緑丘町8-7 横浜リバーテラスビル14階</div>
  </div>

  <div class="abs sister">
    <span class="sister__label">系列園</span>
    <div class="sister__brand"><span class="sister__dot"></span>くるみや保育園</div>
    <div class="sister__url round">https://kurumiya-hoiku.jp/</div>
  </div>

</main>
</body>
</html>
```